Real Estate Flyer

I would like an A4 size flyer which has the same info 3 times and can be cut into three.
It will be used for letterbox drops for new listings (SELLING) and sold listings (SOLD). The flyer needs a heading (as above) and a space for a photo which is able to be changed for each new property. Needs to be blue, red and white. It also requires my photo, KLV logo, Marisska Thornbury logo and the following text:
"Are you considering selling? Call Marisska today for a complimentary market appraisal".
(KLV logo, Marisska Thornbury Sales Consultant logo and my photo can be found in uploaded files)

```html
<!DOCTYPE html>
<html lang="en">
<head>
<meta charset="utf-8">
<title>Real Estate Flyer – Marisska Thornbury</title>
<link rel="stylesheet" href="https://fonts.googleapis.com/css2?family=Open+Sans:wght@400;600;700;800&display=swap">
<style>
  :root {
    --blue: #1f7ac4;
    --blue-dark: #155e9b;
    --red: #e0242b;
    --white: #ffffff;
    --grey-band: #dfe3e8;
    --grey-text: #333333;
    --page: #eeeeee;
  }
  * { box-sizing: border-box; margin: 0; padding: 0; }
  html, body {
    width: 1168px; height: 1200px; overflow: hidden;
    background: var(--page);
    font-family: "Open Sans", Arial, sans-serif;
  }
  .sheet {
    position: absolute; left: 44px; top: 235px;
    display: flex; gap: 24px;
  }
  .flyer {
    position: relative; width: 344px; height: 730px;
    background: var(--white); overflow: hidden;
    box-shadow: 0 4px 14px rgba(0,0,0,0.25);
  }
  .flyer-shapes { position: absolute; inset: 0; }
  .brand-box {
    position: absolute; top: 8px; right: 14px; width: 150px; height: 34px;
    background: var(--blue); border: 2px solid var(--white);
    box-shadow: 0 0 0 1px var(--blue-dark);
    display: flex; align-items: center; justify-content: center;
    color: var(--white); font-weight: 700; font-size: 20px; letter-spacing: 2px;
  }
  .property-photo {
    position: absolute; left: 22px; top: 62px; width: 322px; height: 222px;
    border-radius: 150px 0 0 120px / 111px 0 0 111px;
  }
  .photo-selling { background: linear-gradient(180deg, #8fb8e0 0%, #cfdde6 45%, #b8914f 62%, #6f9a45 100%); }
  .photo-sold { background: linear-gradient(180deg, #a9c9e6 0%, #dfe8ef 40%, #5a7896 60%, #8aa06a 100%); }
  .photo-selling-b { background: linear-gradient(180deg, #b9cfe0 0%, #e6e2d8 40%, #9a7a5e 62%, #b7b0a2 100%); }
  .status-tag {
    position: absolute; top: 58px; left: 14px;
    padding: 6px 16px; background: var(--red); color: var(--white);
    border: 2px solid var(--white); border-radius: 6px;
    box-shadow: 0 2px 4px rgba(0,0,0,0.35);
    font-weight: 800; font-size: 22px; transform: rotate(-10deg);
  }
  .consultant {
    position: absolute; top: 316px; left: 14px;
    display: flex; align-items: center; gap: 8px;
  }
  .consultant-mark { width: 30px; height: 30px; border-radius: 50%; background: var(--red); }
  .consultant-name { font-size: 15px; color: var(--grey-text); line-height: 1.1; }
  .consultant-role { font-size: 9px; color: var(--grey-text); padding-left: 34px; }
  .consultant-phone { font-size: 9px; color: var(--red); padding-left: 44px; }
  .headline {
    position: absolute; top: 372px; left: 0; width: 344px;
    text-align: center; color: var(--white); font-weight: 700; line-height: 1.15;
  }
  .headline-lead { font-size: 25px; letter-spacing: -0.5px; }
  .headline-key { font-size: 32px; }
  .agent-photo {
    position: absolute; left: 29px; top: 500px; width: 109px; height: 140px;
    background: linear-gradient(180deg, #b7b0ab 0%, #8a6e62 45%, #1d1d22 100%);
  }
  .call-to-action {
    position: absolute; left: 148px; top: 522px; width: 190px;
    font-weight: 700; line-height: 1.08;
    text-shadow: 1px 1px 0 #c8c8c8, -1px -1px 0 var(--white);
  }
  .cta-call { font-size: 34px; color: var(--blue); }
  .cta-name { font-size: 29px; color: var(--red); }
  .cta-today { font-size: 25px; color: var(--blue); }
  .appraisal {
    position: absolute; left: 0; top: 644px; width: 344px;
    text-align: center; font-size: 16.5px; font-weight: 600; color: var(--blue);
    letter-spacing: -0.3px;
  }
  .phone-strip {
    position: absolute; left: 0; bottom: 0; width: 344px; height: 56px;
    display: flex; align-items: center; justify-content: center;
    color: var(--white); font-weight: 700; font-size: 28px;
  }
</style>
</head>
<body>
<main class="sheet">

  <article class="flyer">
    <svg class="flyer-shapes" viewBox="0 0 344 730" aria-hidden="true">
      <polygon points="0,24 344,0 344,12 0,38" fill="var(--grey-band)"/>
      <line x1="0" y1="44" x2="344" y2="18" stroke="var(--blue)" stroke-width="3"/>
      <path d="M0,302 Q172,272 344,294" fill="none" stroke="var(--grey-band)" stroke-width="10"/>
      <path d="M0,296 Q172,266 344,288" fill="none" stroke="var(--blue)" stroke-width="4"/>
      <polygon points="0,353 344,313 344,442 0,490" fill="var(--blue)"/>
      <rect x="0" y="674" width="344" height="56" fill="var(--red)"/>
    </svg>
    <div class="brand-box">KLV</div>
    <div class="property-photo photo-selling" role="img" aria-label="Photo of the property for sale"></div>
    <div class="status-tag">SELLING</div>
    <div class="consultant-block">
      <div class="consultant"><span class="consultant-mark"></span><span class="consultant-name">Marisska Thornbury</span></div>
    </div>
    <div class="consultant" style="top:346px;flex-direction:column;align-items:flex-start;gap:0">
      <span class="consultant-role">Sales Consultant</span>
      <span class="consultant-phone">0400 555 019</span>
    </div>
    <h2 class="headline"><span class="headline-lead">ARE YOU CONSIDERING</span><br><span class="headline-key">SELLING ?</span></h2>
    <div class="agent-photo" role="img" aria-label="Portrait photo of Marisska Thornbury"></div>
    <p class="call-to-action"><span class="cta-call">CALL</span><br><span class="cta-name">MARISSKA</span><br><span class="cta-today">TODAY FOR</span></p>
    <p class="appraisal">A COMPLIMENTARY MARKET APPRAISAL</p>
    <p class="phone-strip">0400 555 019</p>
  </article>

  <article class="flyer">
    <svg class="flyer-shapes" viewBox="0 0 344 730" aria-hidden="true">
      <polygon points="0,24 344,0 344,12 0,38" fill="var(--grey-band)"/>
      <line x1="0" y1="44" x2="344" y2="18" stroke="var(--blue)" stroke-width="3"/>
      <path d="M0,302 Q172,272 344,294" fill="none" stroke="var(--grey-band)" stroke-width="10"/>
      <path d="M0,296 Q172,266 344,288" fill="none" stroke="var(--blue)" stroke-width="4"/>
      <polygon points="0,353 344,313 344,442 0,490" fill="var(--blue)"/>
      <rect x="0" y="674" width="344" height="56" fill="var(--red)"/>
    </svg>
    <div class="brand-box">KLV</div>
    <div class="property-photo photo-sold" role="img" aria-label="Photo of the sold property"></div>
    <div class="status-tag">SOLD</div>
    <div class="consultant"><span class="consultant-mark"></span><span class="consultant-name">Marisska Thornbury</span></div>
    <div class="consultant" style="top:346px;flex-direction:column;align-items:flex-start;gap:0">
      <span class="consultant-role">Sales Consultant</span>
      <span class="consultant-phone">0400 555 019</span>
    </div>
    <h2 class="headline"><span class="headline-lead">ARE YOU CONSIDERING</span><br><span class="headline-key">SELLING ?</span></h2>
    <div class="agent-photo" role="img" aria-label="Portrait photo of Marisska Thornbury"></div>
    <p class="call-to-action"><span class="cta-call">CALL</span><br><span class="cta-name">MARISSKA</span><br><span class="cta-today">TODAY FOR</span></p>
    <p class="appraisal">A COMPLIMENTARY MARKET APPRAISAL</p>
    <p class="phone-strip">0400 555 019</p>
  </article>

  <article class="flyer">
    <svg class="flyer-shapes" viewBox="0 0 344 730" aria-hidden="true">
      <polygon points="0,24 344,0 344,12 0,38" fill="var(--grey-band)"/>
      <line x1="0" y1="44" x2="344" y2="18" stroke="var(--blue)" stroke-width="3"/>
      <path d="M0,302 Q172,272 344,294" fill="none" stroke="var(--grey-band)" stroke-width="10"/>
      <path d="M0,296 Q172,266 344,288" fill="none" stroke="var(--blue)" stroke-width="4"/>
      <polygon points="0,353 344,313 344,442 0,490" fill="var(--blue)"/>
      <rect x="0" y="674" width="344" height="56" fill="var(--red)"/>
    </svg>
    <div class="brand-box">KLV</div>
    <div class="property-photo photo-selling-b" role="img" aria-label="Photo of another property for sale"></div>
    <div class="status-tag">SELLING</div>
    <div class="consultant"><span class="consultant-mark"></span><span class="consultant-name">Marisska Thornbury</span></div>
    <div class="consultant" style="top:346px;flex-direction:column;align-items:flex-start;gap:0">
      <span class="consultant-role">Sales Consultant</span>
      <span class="consultant-phone">0400 555 019</span>
    </div>
    <h2 class="headline"><span class="headline-lead">ARE YOU CONSIDERING</span><br><span class="headline-key">SELLING ?</span></h2>
    <div class="agent-photo" role="img" aria-label="Portrait photo of Marisska Thornbury"></div>
    <p class="call-to-action"><span class="cta-call">CALL</span><br><span class="cta-name">MARISSKA</span><br><span class="cta-today">TODAY FOR</span></p>
    <p class="appraisal">A COMPLIMENTARY MARKET APPRAISAL</p>
    <p class="phone-strip">0400 555 019</p>
  </article>

</main>
</body>
</html>
```